New Business Card Design for Manufacturing

We are an engineering/manufacturing company that offers Advanced machining/assembly/engineering services, as well as innovative products for the heavy duty engine cooling markets.

We are looking to get a new business card designed that is clean and modern looking, but still fits the wide range of technical/skilled work we do.

- We hope to use this design as the base for other design work in new Presentations, web, and print work.

Industry/Entity Type

Engineering

Contact Information for Business Card

Our preferred color of blue is (RGB) 22/71/159 but can vary slightly from that color. Our content will be our Logo and full company name (Fabricated Tooling Works, Inc.), company address, name, job title, phone number with extension, cell number, fax number, website, and email address on the cards.
We'd like the full company name next to the logo, but we are open to other interpretations of that layout.
Preferably, we would like the back side to be clean with just our logo, and the front to contain all of the contact information.

Colors
2f74b4
0355a3
85abd2

Requirements
Must have
• - Logo, company name, needed content - We are open to interpretation beyond that.
• - Standard size business card.
• - Horizontal orientation.
• - Enough space for lengthy names / job titles (for example, a job title could read "Directory of Human Resources" or "V.P. of Governmental Affairs"). We need this to look clean, whether the title be short (CEO) or long (as described above).

```html
<!DOCTYPE html>
<html lang="en">
<head>
<meta charset="utf-8">
<title>Fabricated Tooling Works, Inc. – Business Card</title>
<link href="https://fonts.googleapis.com/css2?family=Lato:wght@300;400;700;900&display=swap" rel="stylesheet">
<style>
  :root {
    --brand-blue: #16479f;
    --mid-blue: #0355a3;
    --bright-blue: #2f74b4;
    --pale-blue: #85abd2;
    --paper: #ffffff;
    --paper-shade: #eef0f3;
    --stage: #e6e8ec;
    --ink-soft: #6f8fbf;
  }
  * { box-sizing: border-box; margin: 0; padding: 0; }
  html, body { width: 1200px; height: 780px; overflow: hidden; }
  body {
    background: var(--stage);
    font-family: "Lato", sans-serif;
    display: flex;
    align-items: center;
    justify-content: center;
    gap: 40px;
  }
  .card {
    position: relative;
    width: 540px;
    height: 309px;
    border-radius: 4px;
    overflow: hidden;
    box-shadow: 0 10px 28px rgba(20, 40, 80, 0.18);
  }

  /* Front */
  .card-front { background: linear-gradient(160deg, var(--paper), var(--paper-shade)); }
  .card-front .swoosh { position: absolute; inset: 0; width: 100%; height: 100%; }
  .front-brand {
    position: absolute;
    left: 34px;
    top: 92px;
    display: flex;
    align-items: center;
    gap: 12px;
  }
  .brand-square {
    width: 38px; height: 38px;
    background: var(--brand-blue);
    flex: none;
  }
  .brand-name {
    font-weight: 900;
    font-size: 18px;
    line-height: 1.08;
    letter-spacing: 0.3px;
    text-transform: uppercase;
    color: var(--brand-blue);
  }
  .person {
    position: absolute;
    left: 34px;
    top: 196px;
  }
  .person-name {
    font-weight: 400;
    font-size: 17px;
    letter-spacing: 0.4px;
    text-transform: uppercase;
    color: var(--brand-blue);
  }
  .person-title {
    font-weight: 300;
    font-size: 14px;
    color: var(--ink-soft);
    margin-top: 2px;
  }
  .contact-list {
    position: absolute;
    right: 22px;
    top: 30px;
    list-style: none;
    text-align: right;
    color: #fff;
    font-size: 12.5px;
    font-weight: 400;
  }
  .contact-list li {
    display: flex;
    justify-content: flex-end;
    align-items: center;
    gap: 8px;
    height: 20px;
  }
  .contact-list svg { width: 14px; height: 14px; flex: none; }
  .address {
    position: absolute;
    right: 22px;
    bottom: 24px;
    color: #fff;
    font-size: 12px;
    text-align: right;
    max-width: 220px;
    line-height: 1.4;
  }

  /* Back */
  .card-back {
    background: radial-gradient(ellipse at 40% 30%, var(--bright-blue), var(--mid-blue) 60%, var(--brand-blue));
    display: flex;
    flex-direction: column;
    align-items: center;
    justify-content: center;
    gap: 22px;
  }
  .back-brand { display: flex; align-items: center; gap: 14px; }
  .back-brand .brand-square { background: #fff; width: 46px; height: 46px; }
  .back-brand .brand-name { color: #fff; font-size: 22px; }
  .back-web {
    color: rgba(255,255,255,0.85);
    font-size: 13px;
    letter-spacing: 4px;
  }
</style>
</head>
<body>

<section class="card card-front" aria-label="Business card front">
  <svg class="swoosh" viewBox="0 0 540 309" preserveAspectRatio="none" aria-hidden="true">
    <path d="M318,0 C258,110 262,230 300,309 L540,309 L540,0 Z" fill="var(--pale-blue)" opacity="0.75"/>
    <path d="M338,0 C284,110 292,230 338,309 L540,309 L540,0 Z" fill="var(--mid-blue)"/>
    <path d="M338,0 C284,110 292,230 338,309 L540,309 L540,0 Z" fill="var(--bright-blue)" opacity="0.35"/>
  </svg>

  <div class="front-brand">
    <span class="brand-square"></span>
    <span class="brand-name">Fabricated<br>Tooling Works, Inc.</span>
  </div>

  <div class="person">
    <p class="person-name">Daniel Reyes</p>
    <p class="person-title">Founder</p>
  </div>

  <ul class="contact-list">
    <li>(555) 310-2846
      <svg viewBox="0 0 14 14"><circle cx="7" cy="7" r="6.3" fill="none" stroke="#fff" stroke-width="1"/><rect x="5" y="3.5" width="4" height="7" rx="0.8" fill="#fff"/></svg>
    </li>
    <li>(555) 310-2847
      <svg viewBox="0 0 14 14"><circle cx="7" cy="7" r="6.3" fill="none" stroke="#fff" stroke-width="1"/><path d="M4.5 4 L6 4 L6.6 5.8 L5.7 6.5 Q6.6 8.2 7.8 8.7 L8.5 7.9 L10 8.5 L10 9.8 Q6.5 10.5 4.5 5.5 Z" fill="#fff"/></svg>
    </li>
    <li>hello@ftworks.com
      <svg viewBox="0 0 14 14"><circle cx="7" cy="7" r="6.3" fill="none" stroke="#fff" stroke-width="1"/><rect x="3.8" y="4.8" width="6.4" height="4.4" fill="#fff"/><path d="M3.8 4.8 L7 7.3 L10.2 4.8" fill="none" stroke="var(--mid-blue)" stroke-width="0.7"/></svg>
    </li>
    <li>www.ftworks.com
      <svg viewBox="0 0 14 14"><circle cx="7" cy="7" r="6.3" fill="none" stroke="#fff" stroke-width="1"/><circle cx="7" cy="7" r="3.5" fill="none" stroke="#fff" stroke-width="0.8"/><path d="M3.5 7 H10.5 M7 3.5 V10.5" stroke="#fff" stroke-width="0.8"/></svg>
    </li>
    <li>PO Box 48, Geelong
      <svg viewBox="0 0 14 14"><circle cx="7" cy="7" r="6.3" fill="none" stroke="#fff" stroke-width="1"/><path d="M7 3.5 A2.4 2.4 0 0 1 9.4 5.9 C9.4 7.6 7 10.5 7 10.5 C7 10.5 4.6 7.6 4.6 5.9 A2.4 2.4 0 0 1 7 3.5 Z" fill="#fff"/></svg>
    </li>
  </ul>

  <p class="address">PO Box 48, 210 Harbor Lane, Geelong</p>
</section>

<section class="card card-back" aria-label="Business card back">
  <div class="back-brand">
    <span class="brand-square"></span>
    <span class="brand-name">Fabricated<br>Tooling Works, Inc.</span>
  </div>
  <p class="back-web">www.ftworks.com</p>
</section>

</body>
</html>
```